Garnett and Lyle Personal Injury Billboard

We'd like a clean/modern billboard to build brand awareness for our law firm in the area of personal injury. Ideally, we like the word "Injured?" or something similar in large lettering.

I'm attaching images, logo and award badges which could be used. The billboards will be 14x48 ft and 10.6x36.

We are open to different color ideas, fonts, and artwork. Creative but not too busy with wording. Our web page is www.kgarnettfirm.example

Garnett & Lyle Law Firm
(555) 318-4092

```html
<!DOCTYPE html>
<html lang="en">
<head>
<meta charset="utf-8">
<title>Garnett &amp; Lyle Law Firm — Personal Injury Billboard</title>
<link rel="stylesheet" href="https://fonts.googleapis.com/css2?family=Fira+Sans+Condensed:wght@600;700&family=Fira+Sans:wght@300;400;600&display=swap">
<style>
  :root {
    --page-bg: #ffffff;
    --red-deep: #6e0a0c;
    --red-mid: #a8161b;
    --red-bright: #c9242a;
    --text-light: #ffffff;
    --badge-navy: #1c2f4a;
    --badge-blue: #2aa7e0;
  }
  * { margin: 0; padding: 0; box-sizing: border-box; }
  html, body {
    width: 1025px;
    height: 1200px;
    overflow: hidden;
    background: var(--page-bg);
  }
  .billboard {
    position: absolute;
    left: 30px;
    top: 458px;
    width: 965px;
    height: 284px;
    overflow: hidden;
    box-shadow: 0 8px 10px rgba(0, 0, 0, 0.22);
    color: var(--text-light);
  }
  .billboard-photo {
    position: absolute;
    inset: 0;
    background:
      linear-gradient(180deg, rgba(110, 10, 12, 0.35) 0%, rgba(110, 10, 12, 0) 30%),
      linear-gradient(90deg, var(--red-mid) 0%, var(--red-bright) 30%, var(--red-mid) 55%, var(--red-bright) 78%, var(--red-deep) 100%);
  }
  .firm-name {
    position: absolute;
    left: 20px;
    top: 28px;
    display: flex;
    align-items: center;
    gap: 6px;
    font-family: "Fira Sans", sans-serif;
    font-weight: 600;
    font-size: 13px;
    line-height: 1.1;
    letter-spacing: 0.5px;
    text-transform: uppercase;
  }
  .firm-name .mark {
    width: 10px;
    height: 10px;
    background: var(--text-light);
  }
  .message {
    position: absolute;
    left: 20px;
    right: 0;
    top: 14px;
    text-align: center;
  }
  .headline {
    font-family: "Fira Sans Condensed", sans-serif;
    font-weight: 700;
    font-size: 122px;
    line-height: 1;
    letter-spacing: -1px;
  }
  .subhead {
    font-family: "Fira Sans Condensed", sans-serif;
    font-weight: 700;
    font-size: 66px;
    line-height: 1;
    margin-top: -4px;
  }
  .phone {
    font-family: "Fira Sans", sans-serif;
    font-weight: 300;
    font-size: 28px;
    line-height: 1.2;
    margin-top: 10px;
  }
  .website {
    font-family: "Fira Sans", sans-serif;
    font-weight: 400;
    font-size: 19px;
    letter-spacing: 0.5px;
    margin-top: 4px;
  }
  .award-badge {
    position: absolute;
    right: 23px;
    top: 201px;
    width: 42px;
    height: 60px;
    background: linear-gradient(180deg, var(--badge-blue) 0%, var(--badge-navy) 35%, var(--badge-navy) 80%, var(--badge-blue) 80%);
    border: 1.5px solid var(--text-light);
  }
</style>
</head>
<body>
  <section class="billboard">
    <div class="billboard-photo" role="img" aria-label="Red-toned photo of a classical courthouse facade with ornate columns"></div>

    <div class="firm-name">
      <span class="mark"></span>
      <span>Garnett &amp; Lyle<br>Law Firm</span>
    </div>

    <div class="message">
      <h1 class="headline">INJURED?</h1>
      <p class="subhead">We can help!</p>
      <p class="phone">Call US: (555) 318-4092</p>
      <p class="website">www.kgarnettfirm.example</p>
    </div>

    <div class="award-badge" role="img" aria-label="Community award badge"></div>
  </section>
</body>
</html>
```